Brennick Holdings Business Cards

These are professional business cards that are for my family office.
Put fake emails and phone numbers as of now until I finalize those components. This family office controls my families investments, assets, and future. The cards should be professional.
..
.
.
.
I just uploaded another variation of a logo I would like to see as a business card to I am inbeteen which logo to use

Target Market(s)

business

Industry/Entity Type

business

Contact Information for Business Card

Professional, wealth related, finance related.

Requirements
Must have
• Logo

```html
<!DOCTYPE html>
<html lang="en">
<head>
<meta charset="utf-8">
<title>Brennick Holdings Business Cards</title>
<link rel="stylesheet" href="https://fonts.googleapis.com/css2?family=Montserrat:wght@400;600;700&display=swap">
<style>
  :root {
    --backdrop: #ababab;
    --navy: #181e2a;
    --navy-faint: #252b37;
    --paper: #eaeaea;
    --ink: #111111;
    --ink-soft: #555555;
    --rule: #8a8a8a;
    --band-grey: #a5a3a4;
    --dot-grey: #a8a8a8;
  }
  * { margin: 0; padding: 0; box-sizing: border-box; }
  html, body {
    width: 1200px;
    height: 1000px;
    overflow: hidden;
    background: var(--backdrop);
    font-family: "Montserrat", sans-serif;
  }
  .sheet {
    position: relative;
    width: 1200px;
    height: 1000px;
  }
  .card {
    position: absolute;
    left: 234px;
    width: 733px;
    height: 421px;
    overflow: hidden;
  }
  .card-back {
    top: 57px;
    background: var(--navy);
  }
  .back-name {
    position: absolute;
    right: 48px;
    top: 186px;
    font-weight: 600;
    font-size: 40px;
    letter-spacing: 3px;
    text-transform: uppercase;
    color: var(--navy-faint);
    line-height: 1.1;
    text-align: right;
  }
  .card-front {
    top: 503px;
    background: var(--paper);
  }
  .brand {
    position: absolute;
    top: 66px;
    left: 0;
    width: 100%;
    display: flex;
    justify-content: center;
    align-items: flex-start;
    gap: 8px;
  }
  .brand-name {
    font-weight: 600;
    font-size: 30px;
    letter-spacing: 2px;
    text-transform: uppercase;
    color: var(--ink);
    line-height: 1;
    padding-top: 10px;
  }
  .brand-dot {
    width: 9px;
    height: 9px;
    border-radius: 50%;
    background: var(--dot-grey);
  }
  .person {
    position: absolute;
    right: calc(733px - 342px);
    top: 222px;
    text-align: right;
  }
  .person-name {
    font-weight: 700;
    font-size: 24px;
    color: var(--ink);
    line-height: 1.1;
  }
  .person-role {
    font-weight: 600;
    font-size: 10px;
    letter-spacing: 1.6px;
    text-transform: uppercase;
    color: var(--ink);
    margin-top: 3px;
  }
  .divider {
    position: absolute;
    left: 369px;
    top: 207px;
    width: 2px;
    height: 76px;
    background: var(--rule);
  }
  .contact {
    position: absolute;
    left: 392px;
    top: 207px;
    list-style: none;
    font-weight: 400;
    font-size: 20px;
    line-height: 24.5px;
    color: var(--ink-soft);
  }
  .band {
    position: absolute;
    bottom: 0;
    height: 16px;
  }
  .band-grey { left: 0; width: 370px; background: var(--band-grey); }
  .band-navy { left: 370px; right: 0; background: var(--navy); }
</style>
</head>
<body>
  <main class="sheet">
    <section class="card card-back" aria-label="Card back">
      <div class="back-name">Brennick<br>Holdings</div>
    </section>

    <section class="card card-front" aria-label="Card front">
      <div class="brand">
        <span class="brand-name">Brennick Holdings</span>
        <span class="brand-dot"></span>
      </div>

      <div class="person">
        <div class="person-name">Name Surname</div>
        <div class="person-role">Position</div>
      </div>

      <div class="divider"></div>

      <ul class="contact">
        <li>123 456 7890</li>
        <li>email@website.com</li>
        <li>website.com</li>
      </ul>

      <div class="band band-grey"></div>
      <div class="band band-navy"></div>
    </section>
  </main>
</body>
</html>
```